Reproduce my app screenshot to look more updated and modern

My app is a place for farmers to post jobs a when needing help around the Farm, and local farmhands can apply for the job. The Farmer can then review multiple applicants and select the one best fit for the task at hand. I'm trying to give my screens an updated look while keeping my current color scheme and flow. I would like for you guys to recreate this screen with an updated loo the best you can. The main screen with the QV will stay the same. I put that in there to show our logo and our main colors. They look outdated.

Target Market(s)

Farmers and Farm Emlpoyees inside the US

Industry/Entity Type

Agriculture

Requirements
Must have
• and updated look and same buttom/ functionality
Nice to have
Should not have
• dont change the name of any buttons

```html
<!DOCTYPE html>
<html lang="en">
<head>
<meta charset="utf-8">
<title>Quillvale – Current Jobs</title>
<link href="https://fonts.googleapis.com/css2?family=Open+Sans:ital,wght@0,400;0,600;0,700;1,700&family=Roboto+Condensed:wght@500;700&display=swap" rel="stylesheet">
<style>
  :root {
    --farm-green: #347a36;
    --farm-green-deep: #2a6430;
    --leaf-green: #a6d86a;
    --mile-green: #3f8f3c;
    --mile-tint: #e8f3df;
    --job-purple: #4b3f94;
    --action-lavender: #8a86d4;
    --page: #f3f4f1;
    --segment: #e6e7e2;
    --muted: #8d8f8a;
    --heart-grey: #d6d7d3;
    --ink: #1f2320;
    --nav-dark: #2f3230;
    --white: #ffffff;
  }
  * { box-sizing: border-box; margin: 0; padding: 0; }
  html, body { width: 1200px; height: 2259px; overflow: hidden; }
  body { background: var(--page); font-family: "Open Sans", sans-serif; color: var(--ink); }

  .screen {
    position: absolute; left: 0; top: 0;
    width: 400px; height: 753px;
    transform: scale(3); transform-origin: 0 0;
    background: var(--page); overflow: hidden;
  }

  /* Header */
  .app-header {
    position: absolute; left: 0; top: 0; width: 400px; height: 148px;
    background: linear-gradient(160deg, var(--farm-green) 0%, var(--farm-green-deep) 100%);
    border-radius: 0 0 26px 26px; color: var(--white);
  }
  .status-bar { position: absolute; top: 10px; left: 22px; right: 20px; display: flex; justify-content: space-between; align-items: center; font-size: 11px; font-weight: 600; }
  .status-icons { display: flex; gap: 5px; align-items: center; }
  .brand-row { position: absolute; top: 32px; left: 16px; right: 16px; height: 30px; display: flex; align-items: center; }
  .brand { display: flex; align-items: center; gap: 8px; font-size: 17px; font-weight: 700; letter-spacing: 2px; }
  .brand-dot { width: 10px; height: 10px; border-radius: 50%; background: var(--leaf-green); }
  .menu-button { margin-left: auto; width: 32px; height: 30px; border-radius: 10px; background: rgba(255,255,255,.14); display: flex; align-items: center; justify-content: center; }

  .profile {
    position: absolute; top: 72px; left: 16px; right: 16px; height: 58px;
    background: rgba(255,255,255,.12); border-radius: 16px;
    display: flex; align-items: center; padding: 0 10px;
  }
  .profile-photo { width: 42px; height: 42px; border-radius: 50%; border: 2px solid var(--leaf-green); background: linear-gradient(135deg, #6d8a96, #b58e72 55%, #4d6f86); flex-shrink: 0; }
  .profile-info { margin-left: 10px; }
  .profile-name { font-size: 14px; font-weight: 700; line-height: 18px; }
  .profile-phone { font-size: 11px; line-height: 15px; opacity: .85; }
  .edit-link { margin-left: auto; display: flex; align-items: center; gap: 5px; height: 28px; padding: 0 12px; border-radius: 14px; background: var(--leaf-green); color: var(--farm-green-deep); font-family: "Roboto Condensed", sans-serif; font-weight: 700; font-size: 11px; letter-spacing: .5px; }

  /* Tabs */
  .tab-row { position: absolute; top: 160px; left: 16px; right: 16px; height: 38px; display: flex; gap: 8px; }
  .segments { width: 224px; height: 38px; background: var(--segment); border-radius: 12px; padding: 3px; display: flex; }
  .tab { flex: 1; border-radius: 9px; display: flex; align-items: center; justify-content: center; font-family: "Roboto Condensed", sans-serif; font-size: 13px; font-weight: 700; color: var(--muted); }
  .tab.is-active { background: var(--white); color: var(--farm-green); box-shadow: 0 1px 4px rgba(0,0,0,.1); }
  .post-job { flex: 1; height: 38px; border-radius: 12px; background: var(--action-lavender); color: var(--white); font-family: "Roboto Condensed", sans-serif; font-weight: 700; font-size: 12px; letter-spacing: .3px; display: flex; align-items: center; justify-content: center; gap: 6px; box-shadow: 0 3px 8px rgba(138,134,212,.4); }

  /* Search */
  .search-row { position: absolute; top: 210px; left: 16px; right: 16px; height: 42px; display: flex; gap: 8px; }
  .search-field { flex: 1; height: 42px; border-radius: 14px; background: var(--white); box-shadow: 0 2px 8px rgba(0,0,0,.06); display: flex; align-items: center; padding-left: 14px; gap: 9px; color: var(--muted); font-size: 13px; }
  .filter-button { width: 42px; height: 42px; border-radius: 14px; background: var(--job-purple); display: flex; align-items: center; justify-content: center; }

  /* Job list */
  .job-list { position: absolute; top: 264px; left: 16px; width: 368px; }
  .job-card { position: relative; display: flex; height: 92px; padding: 12px; background: var(--white); border-radius: 16px; margin-bottom: 10px; box-shadow: 0 2px 10px rgba(0,0,0,.06); }
  .job-card.is-tall { height: 108px; }
  .job-card.is-peek { height: 92px; }
  .job-dates { width: 60px; flex-shrink: 0; border-radius: 12px; background: var(--job-purple); color: var(--white); display: flex; flex-direction: column; align-items: center; justify-content: center; font-family: "Roboto Condensed", sans-serif; font-weight: 700; text-align: center; }
  .job-date .day { display: block; font-size: 16px; line-height: 17px; }
  .job-date .month { display: block; font-size: 9.5px; line-height: 11px; letter-spacing: .6px; opacity: .85; }
  .job-dates .dash { width: 14px; height: 2px; border-radius: 1px; background: var(--leaf-green); margin: 4px 0; }
  .job-info { margin-left: 14px; width: 226px; }
  .job-title { font-size: 14px; font-weight: 700; line-height: 17px; }
  .job-row { display: flex; align-items: center; gap: 5px; font-size: 11px; line-height: 16px; color: #4d514c; }
  .job-row svg { flex-shrink: 0; }
  .miles { color: var(--mile-green); background: var(--mile-tint); border-radius: 8px; padding: 0 6px; font-size: 10px; font-weight: 600; line-height: 14px; }
  .job-rate { font-size: 11px; font-weight: 700; line-height: 16px; color: var(--ink); }
  .favorite { position: absolute; right: 12px; top: 12px; width: 30px; height: 30px; border-radius: 50%; background: #f3f4f1; display: flex; align-items: center; justify-content: center; }

  .favorites-fab { position: absolute; left: 330px; top: 624px; width: 48px; height: 48px; border-radius: 16px; background: var(--leaf-green); display: flex; align-items: center; justify-content: center; box-shadow: 0 4px 12px rgba(52,122,54,.35); }

  /* Bottom nav */
  .bottom-nav { position: absolute; left: 12px; top: 688px; width: 376px; height: 56px; border-radius: 20px; background: var(--nav-dark); display: flex; align-items: center; padding: 0 6px; box-shadow: 0 6px 16px rgba(0,0,0,.2); }
  .nav-item { flex: 1; height: 46px; border-radius: 14px; display: flex; flex-direction: column; align-items: center; justify-content: center; gap: 3px; font-family: "Roboto Condensed", sans-serif; font-weight: 700; font-size: 8.5px; letter-spacing: .3px; color: #a3a6a1; }
  .nav-item.is-active { background: var(--farm-green); color: var(--white); }
</style>
</head>
<body>
<main class="screen">
  <header class="app-header">
    <div class="status-bar">
      <span>5:30</span>
      <span class="status-icons">
        <svg width="14" height="9" viewBox="0 0 14 9"><rect x="0" y="6" width="2.5" height="3" fill="#fff"/><rect x="3.8" y="4" width="2.5" height="5" fill="#fff"/><rect x="7.6" y="2" width="2.5" height="7" fill="#fff"/><rect x="11.4" y="0" width="2.5" height="9" fill="#fff"/></svg>
        <svg width="13" height="9" viewBox="0 0 13 9"><path d="M6.5 9 L4.5 6.6 A3 3 0 0 1 8.5 6.6Z M2.6 4.6 A5.6 5.6 0 0 1 10.4 4.6 L9.3 5.7 A4 4 0 0 0 3.7 5.7Z M0.6 2.6 A8.5 8.5 0 0 1 12.4 2.6 L11.3 3.7 A7 7 0 0 0 1.7 3.7Z" fill="#fff"/></svg>
        <svg width="22" height="10" viewBox="0 0 22 10"><rect x="0.5" y="0.5" width="19" height="9" rx="2" fill="none" stroke="#fff"/><rect x="2" y="2" width="16" height="6" rx="1" fill="#fff"/><rect x="20.3" y="3" width="1.5" height="4" fill="#fff"/></svg>
      </span>
    </div>
    <div class="brand-row">
      <div class="brand"><span class="brand-dot"></span>QUILLVALE</div>
      <div class="menu-button">
        <svg width="16" height="12" viewBox="0 0 16 12"><rect width="16" height="2" rx="1" fill="#fff"/><rect y="5" width="16" height="2" rx="1" fill="#fff"/><rect y="10" width="10" height="2" rx="1" fill="#fff"/></svg>
      </div>
    </div>
    <div class="profile">
      <div class="profile-photo" role="img" aria-label="Profile photo of the farmer"></div>
      <div class="profile-info">
        <div class="profile-name">Daniel Hartwell</div>
        <div class="profile-phone">5550148392</div>
      </div>
      <div class="edit-link">
        <svg width="11" height="11" viewBox="0 0 12 12"><path d="M1 9 L8 2 L10 4 L3 11 L1 11Z" fill="#2a6430"/></svg>
        EDIT
      </div>
    </div>
  </header>

  <nav class="tab-row">
    <div class="segments">
      <div class="tab is-active">Current Jobs</div>
      <div class="tab">Nearby Farmhands</div>
    </div>
    <div class="post-job">
      <svg width="10" height="10" viewBox="0 0 10 10"><rect x="4" width="2" height="10" rx="1" fill="#fff"/><rect y="4" width="10" height="2" rx="1" fill="#fff"/></svg>
      POST NEW JOB
    </div>
  </nav>

  <div class="search-row">
    <div class="search-field">
      <svg width="16" height="16" viewBox="0 0 17 17"><circle cx="7" cy="7" r="5.3" fill="none" stroke="#8d8f8a" stroke-width="2"/><path d="M11 11 L15.5 15.5" stroke="#8d8f8a" stroke-width="2.2" stroke-linecap="round"/></svg>
      search...
    </div>
    <div class="filter-button">
      <svg width="15" height="15" viewBox="0 0 15 16"><path d="M0 0 H15 L9 7 V16 L6 13.5 V7Z" fill="#fff"/></svg>
    </div>
  </div>

  <section class="job-list">
    <article class="job-card">
      <div class="job-dates">
        <span class="job-date"><span class="day">01</span><span class="month">APR</span></span>
        <span class="dash"></span>
        <span class="job-date"><span class="day">15</span><span class="month">DEC</span></span>
      </div>
      <div class="job-info">
        <div class="job-title">Seasonal Farm Labor</div>
        <div class="job-row"><svg width="9" height="11" viewBox="0 0 9 11"><path d="M4.5 11 C1.5 7 0 5.5 0 4.2 A4.5 4.2 0 0 1 9 4.2 C9 5.5 7.5 7 4.5 11Z" fill="#8d8f8a"/><circle cx="4.5" cy="4.2" r="1.6" fill="#fff"/></svg>Dewitt, Iowa <span class="miles">2.92 miles</span></div>
        <div class="job-row"><svg width="10" height="10" viewBox="0 0 10 10"><circle cx="5" cy="5" r="4.2" fill="none" stroke="#8d8f8a" stroke-width="1.4"/><path d="M5 2.6 V5 H7" fill="none" stroke="#8d8f8a" stroke-width="1.3"/></svg>08:00am - 05:00pm</div>
        <div class="job-rate">Hourly Rate: $12 - 20</div>
      </div>
      <div class="favorite"><svg width="16" height="14" viewBox="0 0 24 21"><path d="M12 21 L2 11 A6 6 0 0 1 12 3 A6 6 0 0 1 22 11Z" fill="#d6d7d3"/></svg></div>
    </article>

    <article class="job-card">
      <div class="job-dates">
        <span class="job-date"><span class="day">01</span><span class="month">MAR</span></span>
        <span class="dash"></span>
        <span class="job-date"><span class="day">28</span><span class="month">FEB</span></span>
      </div>
      <div class="job-info">
        <div class="job-title">Truck Driver</div>
        <div class="job-row"><svg width="9" height="11" viewBox="0 0 9 11"><path d="M4.5 11 C1.5 7 0 5.5 0 4.2 A4.5 4.2 0 0 1 9 4.2 C9 5.5 7.5 7 4.5 11Z" fill="#8d8f8a"/><circle cx="4.5" cy="4.2" r="1.6" fill="#fff"/></svg>Dewitt, Iowa <span class="miles">2.92 miles</span></div>
        <div class="job-row"><svg width="10" height="10" viewBox="0 0 10 10"><circle cx="5" cy="5" r="4.2" fill="none" stroke="#8d8f8a" stroke-width="1.4"/><path d="M5 2.6 V5 H7" fill="none" stroke="#8d8f8a" stroke-width="1.3"/></svg>03:00pm - 12:00am</div>
        <div class="job-rate">Hourly Rate: $15 - 25</div>
      </div>
      <div class="favorite"><svg width="16" height="14" viewBox="0 0 24 21"><path d="M12 21 L2 11 A6 6 0 0 1 12 3 A6 6 0 0 1 22 11Z" fill="#d6d7d3"/></svg></div>
    </article>

    <article class="job-card is-tall">
      <div class="job-dates">
        <span class="job-date"><span class="day">31</span><span class="month">JAN</span></span>
        <span class="dash"></span>
        <span class="job-date"><span class="day">31</span><span class="month">DEC</span></span>
      </div>
      <div class="job-info">
        <div class="job-title">Farm Hand, Sprayer, Truck, Repair</div>
        <div class="job-row"><svg width="9" height="11" viewBox="0 0 9 11"><path d="M4.5 11 C1.5 7 0 5.5 0 4.2 A4.5 4.2 0 0 1 9 4.2 C9 5.5 7.5 7 4.5 11Z" fill="#8d8f8a"/><circle cx="4.5" cy="4.2" r="1.6" fill="#fff"/></svg>Dewitt, Iowa <span class="miles">6.09 miles</span></div>
        <div class="job-row"><svg width="10" height="10" viewBox="0 0 10 10"><circle cx="5" cy="5" r="4.2" fill="none" stroke="#8d8f8a" stroke-width="1.4"/><path d="M5 2.6 V5 H7" fill="none" stroke="#8d8f8a" stroke-width="1.3"/></svg>01:00pm - 10:00pm</div>
        <div class="job-rate">Hourly Rate: $16 - 22</div>
      </div>
      <div class="favorite"><svg width="16" height="14" viewBox="0 0 24 21"><path d="M12 21 L2 11 A6 6 0 0 1 12 3 A6 6 0 0 1 22 11Z" fill="#d6d7d3"/></svg></div>
    </article>

    <article class="job-card">
      <div class="job-dates">
        <span class="job-date"><span class="day">16</span><span class="month">JAN</span></span>
        <span class="dash"></span>
        <span class="job-date"><span class="day">08</span><span class="month">MAY</span></span>
      </div>
      <div class="job-info">
        <div class="job-title">Farm Management</div>
        <div class="job-row"><svg width="9" height="11" viewBox="0 0 9 11"><path d="M4.5 11 C1.5 7 0 5.5 0 4.2 A4.5 4.2 0 0 1 9 4.2 C9 5.5 7.5 7 4.5 11Z" fill="#8d8f8a"/><circle cx="4.5" cy="4.2" r="1.6" fill="#fff"/></svg>Dewitt, Iowa <span class="miles">4.54 miles</span></div>
        <div class="job-row"><svg width="10" height="10" viewBox="0 0 10 10"><circle cx="5" cy="5" r="4.2" fill="none" stroke="#8d8f8a" stroke-width="1.4"/><path d="M5 2.6 V5 H7" fill="none" stroke="#8d8f8a" stroke-width="1.3"/></svg>09:00am - 18:00pm</div>
        <div class="job-rate">Hourly Rate: $10 - 16</div>
      </div>
      <div class="favorite"><svg width="16" height="14" viewBox="0 0 24 21"><path d="M12 21 L2 11 A6 6 0 0 1 12 3 A6 6 0 0 1 22 11Z" fill="#d6d7d3"/></svg></div>
    </article>
  </section>

  <div class="favorites-fab">
    <svg width="22" height="19" viewBox="0 0 24 21"><path d="M12 21 L2 11 A6 6 0 0 1 12 3 A6 6 0 0 1 22 11Z" fill="#fff"/></svg>
  </div>

  <nav class="bottom-nav">
    <div class="nav-item is-active">
      <svg width="18" height="17" viewBox="0 0 24 22"><path d="M12 0 L24 11 H21 V22 H14.5 V15 H9.5 V22 H3 V11 H0Z" fill="#fff"/></svg>
      HOME
    </div>
    <div class="nav-item">
      <svg width="17" height="17" viewBox="0 0 22 22"><circle cx="9" cy="9" r="7" fill="none" stroke="#a3a6a1" stroke-width="2.6"/><path d="M14 14 L20 20" stroke="#a3a6a1" stroke-width="3" stroke-linecap="round"/></svg>
      SEARCH
    </div>
    <div class="nav-item">
      <svg width="17" height="17" viewBox="0 0 22 22"><rect x="5" y="0" width="16" height="19" rx="2" fill="#a3a6a1"/><rect x="1" y="3" width="16" height="19" rx="2" fill="#a3a6a1" stroke="#2f3230" stroke-width="1.5"/><rect x="4" y="8" width="10" height="1.5" fill="#2f3230"/><rect x="4" y="12" width="10" height="1.5" fill="#2f3230"/><rect x="4" y="16" width="7" height="1.5" fill="#2f3230"/></svg>
      MY JOBS
    </div>
    <div class="nav-item">
      <svg width="22" height="17" viewBox="0 0 28 22"><path d="M0 5 L6 3 L11 12 L5 15Z M28 5 L22 3 L17 12 L23 15Z M8 5 L14 4 L20 6 L22 12 L15 19 L12 19 L6 13Z" fill="#a3a6a1"/></svg>
      FARMHANDS
    </div>
    <div class="nav-item">
      <svg width="17" height="17" viewBox="0 0 22 22"><rect x="1" y="3" width="20" height="19" rx="2" fill="#a3a6a1"/><rect x="5" y="0" width="2.5" height="5" fill="#a3a6a1"/><rect x="14.5" y="0" width="2.5" height="5" fill="#a3a6a1"/><rect x="3" y="8" width="16" height="1.5" fill="#2f3230"/><rect x="5" y="12" width="3" height="3" fill="#2f3230"/><rect x="9.5" y="12" width="3" height="3" fill="#2f3230"/><rect x="14" y="12" width="3" height="3" fill="#2f3230"/><rect x="5" y="16.5" width="3" height="3" fill="#2f3230"/><rect x="9.5" y="16.5" width="3" height="3" fill="#2f3230"/></svg>
      CALENDAR
    </div>
  </nav>
</main>
</body>
</html>
```